Harbourlight Campus Lodgings needs a business card design

Hi Guys,

We are a Student Accommodation company in Australia. We already have a logo which I will submit.

I will require the design of the business cards from you.

I am after something that looks clean, modern and that people feel interested and actually want to contact us.

We would like to see designs that are innovative.

On the business cards I will require to have:

Employee Name
Position
Phone number
Email
Facebook page

I hope you can help me with this project guys as I have heard really good things from you.

```html
<!DOCTYPE html>
<html lang="en">
<head>
<meta charset="utf-8">
<title>Harbourlight Campus Lodgings – Business Card</title>
<link rel="stylesheet" href="https://fonts.googleapis.com/css2?family=Lato:wght@400;700;900&display=swap">
<style>
  :root {
    --brand-green: #0b9339;
    --brand-gold: #f0b02c;
    --card-white: #ffffff;
    --ink: #1c1c1c;
    --stage: #e4e4e4;
  }
  * { box-sizing: border-box; margin: 0; padding: 0; }
  html, body { width: 1200px; height: 680px; overflow: hidden; }
  body {
    background: var(--stage);
    font-family: "Lato", Arial, sans-serif;
    display: flex;
    align-items: center;
    justify-content: center;
    gap: 40px;
  }
  .card {
    position: relative;
    width: 540px;
    height: 308px;
    border-radius: 18px;
    overflow: hidden;
    box-shadow: 0 4px 14px rgba(0,0,0,0.18);
  }

  /* Front */
  .card-front { background: var(--card-white); }
  .card-front .swoosh { position: absolute; inset: 0; width: 100%; height: 100%; }
  .brand-front {
    position: absolute;
    left: 44px;
    top: 104px;
    display: flex;
    align-items: center;
    gap: 10px;
  }
  .brand-mark {
    width: 16px;
    height: 16px;
    background: var(--brand-gold);
    flex: none;
  }
  .brand-name {
    font-weight: 900;
    font-size: 19px;
    line-height: 1.1;
    text-transform: uppercase;
    letter-spacing: 0.5px;
    width: 150px;
  }
  .brand-front .brand-name { color: var(--brand-green); }

  .contact {
    position: absolute;
    left: 288px;
    top: 38px;
  }
  .contact-name { font-size: 19px; color: var(--ink); font-weight: 400; }
  .contact-role { font-size: 14px; color: var(--brand-green); margin: 2px 0 0 12px; }
  .contact-list { list-style: none; margin-top: 8px; }
  .contact-list li {
    display: flex;
    align-items: center;
    gap: 10px;
    font-size: 14px;
    line-height: 18px;
    color: var(--ink);
    margin-top: 4px;
  }
  .contact-list li:first-child { margin-bottom: 12px; }
  .contact-list svg { width: 14px; height: 14px; fill: var(--brand-green); flex: none; }

  /* Back */
  .card-back { background: var(--brand-green); }
  .brand-back {
    position: absolute;
    left: 0; right: 0;
    top: 96px;
    display: flex;
    justify-content: center;
    align-items: center;
    gap: 14px;
  }
  .brand-back .brand-mark { width: 22px; height: 22px; }
  .brand-back .brand-name { color: var(--card-white); font-size: 28px; width: 230px; }
  .social-link {
    position: absolute;
    left: 0; right: 0;
    bottom: 40px;
    text-align: center;
    color: var(--card-white);
    font-size: 15px;
    letter-spacing: 2px;
  }
</style>
</head>
<body>
  <article class="card card-front">
    <svg class="swoosh" viewBox="0 0 540 308" preserveAspectRatio="none" aria-hidden="true">
      <path d="M0 262 C180 244 380 220 540 180 L540 190 C380 232 180 256 0 272 Z" fill="var(--brand-green)"/>
      <path d="M0 272 C180 258 380 236 520 194 C400 252 230 290 150 308 L0 308 Z" fill="var(--brand-gold)"/>
    </svg>
    <div class="brand-front">
      <span class="brand-mark"></span>
      <span class="brand-name">Harbourlight Campus Lodgings</span>
    </div>
    <div class="contact">
      <p class="contact-name">Marcus Tellwright</p>
      <p class="contact-role">manager</p>
      <ul class="contact-list">
        <li>
          <svg viewBox="0 0 24 24"><path d="M6.6 10.8a15.1 15.1 0 0 0 6.6 6.6l2.2-2.2a1 1 0 0 1 1-.25 11.4 11.4 0 0 0 3.6.57 1 1 0 0 1 1 1V20a1 1 0 0 1-1 1A17 17 0 0 1 3 4a1 1 0 0 1 1-1h3.5a1 1 0 0 1 1 1c0 1.25.2 2.45.57 3.57a1 1 0 0 1-.25 1z"/></svg>
          <span>040 555 0173</span>
        </li>
        <li>
          <svg viewBox="0 0 24 24"><path d="M2 5h20v14H2z M2 5l10 8 10-8" stroke="#fff" stroke-width="1.5"/></svg>
          <span>info@harbourlight.com.au</span>
        </li>
        <li>
          <svg viewBox="0 0 24 24"><circle cx="12" cy="7" r="5"/><path d="M3 23c0-6 4-9 9-9s9 3 9 9z"/></svg>
          <span>harbourlight.page/lodgings</span>
        </li>
      </ul>
    </div>
  </article>

  <article class="card card-back">
    <div class="brand-back">
      <span class="brand-mark"></span>
      <span class="brand-name">Harbourlight Campus Lodgings</span>
    </div>
    <p class="social-link">harbourlight.page/lodgings</p>
  </article>
</body>
</html>
```